Handout for attendees of educational seminar

I provide educational workshops on how to give technical presentations at conferences to scientists and engineers. My company is called Craft Talk Studio (www.CraftTalkStudio.example). I would like a double sided, half page size flyer that can be used as a handout for attendees of my workshops. On one side of the flyer, they will get top tips for creating their next presentation. On the other side, they will get my photo, bio, and contact information. I have uploaded a draft of a full page design I made myself. I'd like the copy of the tips to remain the same, but everything else is flexible.

Target Market(s)

scientists, engineers, technical professionals

Font styles to use
Serif
Sans Serif

Requirements
Must have
• my photo (I've provided two options to choose from depending on colors...photo on side 2 only), my logo, flyer needs to be half page in size (5.5" x 8.5"), needs to be double sided, One side has the "tips" and the other side has my personal details (see attached page for copy).
Nice to have
• I like the use of icons on the "tips" side of the flyer.

```html
<!DOCTYPE html>
<html lang="en">
<head>
<meta charset="utf-8">
<title>Craft Talk Studio – Workshop Handout</title>
<link rel="stylesheet" href="https://fonts.googleapis.com/css2?family=Barlow+Condensed:wght@300;400;600&family=Barlow:wght@400;600;700&display=swap">
<style>
  :root {
    --stage: #bcbec0;
    --frame: #8fae6a;
    --paper: #ffffff;
    --ink: #1f1f1f;
    --muted: #4a4a4a;
    --brand: #8fae6a;
    --badge: #555555;
    --photo-a: #4a1c3d;
    --photo-b: #b02a45;
    --photo-c: #3b1f5c;
  }
  * { box-sizing: border-box; margin: 0; padding: 0; }
  html, body { width: 1200px; height: 1000px; overflow: hidden; }
  body { background: var(--stage); position: relative; font-family: "Barlow", sans-serif; color: var(--ink); }

  .sheet { position: absolute; top: 79px; width: 546px; height: 842px; background: var(--paper); border: 9px solid var(--frame); }
  .sheet--tips { left: 46px; }
  .sheet--bio { left: 608px; }

  .contact { position: absolute; font-size: 9px; color: var(--ink); letter-spacing: .2px; }

  .brand { position: absolute; width: 200px; text-align: center; }
  .brand__dot { width: 36px; height: 36px; border-radius: 50%; background: var(--badge); margin: 0 auto 4px; }
  .brand__name { font-family: "Barlow", sans-serif; font-weight: 400; font-size: 12px; color: var(--brand); line-height: 1; }
  .brand__tag { font-size: 6px; letter-spacing: 1px; color: var(--brand); margin-top: 2px; }

  .title { position: absolute; left: 0; width: 100%; top: 106px; text-align: center; font-family: "Barlow Condensed", sans-serif; font-weight: 600; font-size: 40px; letter-spacing: .5px; }
  .subtitle { position: absolute; left: 0; width: 100%; top: 154px; text-align: center; font-family: "Barlow Condensed", sans-serif; font-size: 15px; letter-spacing: .5px; color: var(--muted); }

  .tip { position: absolute; left: 65px; width: 420px; }
  .tip__num { position: absolute; left: 0; top: 0; width: 122px; height: 121px; border: 1.5px solid var(--frame); display: flex; align-items: center; justify-content: center; font-family: "Barlow Condensed", sans-serif; font-weight: 400; font-size: 58px; }
  .tip__icon { position: absolute; left: 121px; top: 0; width: 59px; height: 59px; border: 1.5px solid var(--frame); border-left: none; display: flex; align-items: center; justify-content: center; }
  .tip__heading { position: absolute; left: 138px; top: 82px; font-family: "Barlow Condensed", sans-serif; font-weight: 600; font-size: 17px; letter-spacing: .3px; white-space: nowrap; }
  .tip__body { position: absolute; left: 138px; top: 109px; width: 272px; font-size: 9.5px; line-height: 14px; color: var(--muted); }
  .tip__body p + p { margin-top: 10px; }
  .tip__body strong { color: var(--ink); }

  .photo { position: absolute; left: 0; top: 0; width: 528px; height: 353px; background: radial-gradient(ellipse at 60% 40%, var(--photo-b), var(--photo-a) 60%, var(--photo-c)); }
  .quote-band { position: absolute; left: 0; top: 243px; width: 528px; height: 110px; background: rgba(20, 10, 20, .35); border-top: 19px solid rgba(143, 174, 106, .75); }
  .quote { position: absolute; left: 0; top: 260px; width: 528px; text-align: center; color: #fff; font-family: "Barlow Condensed", sans-serif; font-weight: 300; font-size: 31px; line-height: 41px; letter-spacing: .5px; }

  .bio { position: absolute; left: 77px; top: 394px; width: 380px; }
  .bio__heading { font-size: 13px; font-weight: 700; margin-bottom: 10px; }
  .bio p { font-size: 9.3px; line-height: 14.5px; color: var(--muted); margin-bottom: 10px; }

  .services { position: absolute; left: 39px; top: 649px; width: 452px; height: 48px; border: 1.5px solid var(--frame); display: flex; align-items: center; justify-content: center; text-align: center; font-size: 10px; font-weight: 700; letter-spacing: .3px; line-height: 14px; padding: 0 30px; }
</style>
</head>
<body>

<section class="sheet sheet--tips">
  <span class="contact" style="left:37px;top:33px;">dana@crafttalkstudio.example</span>
  <span class="contact" style="right:37px;top:33px;">www.CraftTalkStudio.example</span>
  <div class="brand" style="left:164px;top:30px;">
    <div class="brand__dot"></div>
    <div class="brand__name">Dana Whitfield</div>
    <div class="brand__tag">Craft Talk Studio</div>
  </div>

  <h1 class="title">QUICK TIPS</h1>
  <div class="subtitle">CRAFT TALK STUDIO</div>

  <article class="tip" style="top:205px;">
    <div class="tip__num">01</div>
    <div class="tip__icon">
      <svg width="32" height="32" viewBox="0 0 32 32" fill="none" stroke="#333" stroke-width="1.2">
        <circle cx="16" cy="6" r="3"/><path d="M11 14c0-3 2-4 5-4s5 1 5 4"/>
        <rect x="9" y="14" width="14" height="6"/>
        <circle cx="8" cy="24" r="2"/><circle cx="16" cy="24" r="2"/><circle cx="24" cy="24" r="2"/>
        <path d="M5 30c0-2 1-3 3-3s3 1 3 3M13 30c0-2 1-3 3-3s3 1 3 3M21 30c0-2 1-3 3-3s3 1 3 3"/>
      </svg>
    </div>
    <h2 class="tip__heading">BE AUDIENCE CENTERED</h2>
    <div class="tip__body">
      <p>Your ability to be successful as a speaker depends upon your ability to make your audience successful.</p>
      <p><strong>TIP:</strong> Return to “Points of Common Ground” throughout the talk that answer the question “So what?” about the scientific info. Be an interpreter!</p>
    </div>
  </article>

  <article class="tip" style="top:414px;">
    <div class="tip__num">02</div>
    <div class="tip__icon">
      <svg width="32" height="32" viewBox="0 0 32 32" fill="none" stroke="#333" stroke-width="1.2">
        <circle cx="16" cy="16" r="12"/><circle cx="16" cy="16" r="8"/>
        <path d="M16 2v5M16 25v5M2 16h5M25 16h5"/>
        <path d="M16 12l-3.5 4h2v4h3v-4h2z"/>
      </svg>
    </div>
    <h2 class="tip__heading">FILTER &amp; FOCUS</h2>
    <div class="tip__body">
      <p>When you try to share everything, you share nothing.</p>
      <p><strong>TIP:</strong> Start your planning with the “view” you want your audience to have at the end of the talk. Then ask yourself “What would they need to know in order to get there?”</p>
    </div>
  </article>

  <article class="tip" style="top:607px;">
    <div class="tip__num">03</div>
    <div class="tip__icon">
      <svg width="32" height="32" viewBox="0 0 32 32" fill="none" stroke="#333" stroke-width="1.2">
        <circle cx="16" cy="16" r="13" stroke-dasharray="2 2"/>
        <path d="M5 16c3-5 7-7 11-7s8 2 11 7c-3 5-7 7-11 7s-8-2-11-7z"/>
        <circle cx="16" cy="16" r="4"/><circle cx="16" cy="16" r="1.5" fill="#333"/>
      </svg>
    </div>
    <h2 class="tip__heading">SHOW YOUR SCIENCE</h2>
    <div class="tip__body">
      <p>Your slides should do something for you that your words cannot. This means make your slides VISUAL not VERBAL.</p>
      <p><strong>TIP:</strong> NO BULLET POINTS (seriously!). Have a brief take-away messages supported by visual evidence.</p>
    </div>
  </article>
</section>

<section class="sheet sheet--bio">
  <div class="photo" role="img" aria-label="Photo of the speaker presenting on a conference stage with a large screen behind her"></div>
  <div class="quote-band"></div>
  <p class="quote">SCIENCE NOT COMMUNICATED<br>IS SCIENCE NOT DONE.</p>

  <div class="bio">
    <h2 class="bio__heading">Meet Dana</h2>
    <p>Dana Whitfield is on a mission: to transform how scientists, engineers, and technical professionals present their work. That’s because she believes that even the best technical ideas are destined to remain undiscovered unless presented in a clear and compelling way that sparks innovation and drives adoption.</p>
    <p>For a decade, she’s traveled around the world to work with Fortune 100 corporations, institutions and universities, teaching the proven strategies she’s mastered through her consulting work and during her time as a faculty member Northgate State University.</p>
    <p>Dana is internationally known for her popular conference talk entitled “Speak Plainly to Me” which has over 2 million views (and counting!).</p>
    <p>Teams that work with Dana get the practical skills and natural confidence they need to immediately shift their “information dump”-style presentations into ones that are meaningful, engaging, and inspire people to take action.</p>
  </div>

  <div class="services">DANA PROVIDES ON-SITE GROUP WORKSHOPS AND COACHING, CONFERENCE SESSIONS AND KEYNOTES, AND 1:1 CONSULTATION.</div>

  <div class="brand" style="left:164px;top:716px;">
    <div class="brand__dot"></div>
    <div class="brand__name">Dana Whitfield</div>
    <div class="brand__tag">Craft Talk Studio</div>
  </div>
  <span class="contact" style="left:37px;top:786px;">dana@crafttalkstudio.example</span>
  <span class="contact" style="right:37px;top:786px;">www.CraftTalkStudio.example</span>
</section>

</body>
</html>
```